Rebranding Website – Tamsel Health Institute (40 Years)

Organization Description:
The Tamsel Health Institute (THI / www.tamselhi.nl) has been a trusted address for more than 40 years for people who choose a natural and sustainable approach to their health. We combine experience and history with a modern, professional approach.

Assignment:
Our current website is outdated and no longer reflects who we are today. We are looking for a new web design that aligns with our renewed logo and is both functional and inspiring. The website should have a clear structure, be user-friendly, and convey trust.

What we are looking for in the design:

A modern, fresh look that matches our logo and color palette logo in attachment.

Goal-oriented: simple and intuitive appointment scheduling.

Informative: space for a blog/news section to share knowledge and updates.

A dedicated page for each therapist with photo, expertise, and contact options.

A separate page for each type of therapy, with explanations and benefits.

A clear and visible link to our webshop (separate website).

Clear navigation and an organized menu structure.

Responsive design (desktop, tablet, mobile).

User-friendly CMS so we can manage and expand content ourselves.

Style Preferences:

- Color palette in line with our logo (green and natural tones, complemented by fresh and calm accents).
- Clean, professional design with plenty of white space.
- Accessible, warm, and inviting.

Functionalities:
- Online appointment scheduling or easy contact options.
- Blog/news section.
- Dedicated pages for therapists and therapies.
- Link to webshop.
- Possibility to expand the offer in the future (e.g., videos, downloads, or e-consultations).

What we would like to avoid:
- Pages that are too cluttered or confusing.
- Excessive text without clear structure.
- Stock photos lacking authenticity.

Target Audience:
People who consciously focus on their health, choose a natural approach, and are looking for a professional and reliable center where expertise and personal attention are central.

Additional Information:
The new website should bridge our 40-year history with the future. A place where visitors feel both familiar and inspired – and where they are immediately invited to get in touch, book an appointment, or visit our webshop.

You find our logo and impression in the uploads.

```html
<!DOCTYPE html>
<html lang="en">
<head>
<meta charset="UTF-8">
<title>Tamsel Health Institute – Knowledge Center</title>
<link href="https://fonts.googleapis.com/css2?family=Lora:wght@400;500&family=Montserrat:wght@600;700&display=swap" rel="stylesheet">
<style>
  :root {
    --green-dark: #4a5e23;
    --green-lime: #8cc63f;
    --text-body: #555a52;
    --text-nav: #3c3f3a;
    --bg-soft: #f7f7f9;
    --white: #ffffff;
  }
  * { margin: 0; padding: 0; box-sizing: border-box; }
  html, body { width: 1200px; height: 960px; overflow: hidden; }
  body { background: var(--white); font-family: 'Lora', serif; position: relative; }

  .site-header {
    position: absolute; top: 0; left: 0; width: 1200px; height: 81px;
    background: var(--white); box-shadow: 0 2px 10px rgba(0,0,0,0.08); z-index: 2;
  }
  .brand { position: absolute; left: 22px; top: 18px; display: flex; align-items: center; gap: 8px; }
  .brand-dot { width: 44px; height: 44px; border: 2px solid var(--green-lime); border-radius: 50%; }
  .brand-name { font-family: 'Montserrat', sans-serif; font-weight: 700; font-size: 16px; color: var(--green-dark); }
  .main-nav a {
    position: absolute; top: 30px; font-size: 16px; color: var(--text-nav); text-decoration: none;
  }
  .main-nav a.active::after {
    content: ""; position: absolute; left: 0; right: 0; bottom: -6px; height: 2px; background: var(--green-lime);
  }
  .webshop-link {
    position: absolute; left: 875px; top: 30px; font-size: 16px; font-weight: 500;
    color: var(--green-dark); text-decoration: none;
  }
  .book-btn {
    position: absolute; left: 986px; top: 21px; width: 178px; height: 41px;
    background: var(--green-lime); color: var(--white); border-radius: 6px;
    font-family: 'Montserrat', sans-serif; font-weight: 700; font-size: 14px;
    display: flex; align-items: center; justify-content: center; text-decoration: none;
    box-shadow: 0 3px 8px rgba(140,198,63,0.35);
  }

  .knowledge {
    position: absolute; top: 0; left: 0; width: 1200px; height: 828px; background: var(--bg-soft);
  }
  .section-title {
    position: absolute; left: 0; width: 1200px; text-align: center;
    font-family: 'Montserrat', sans-serif; font-weight: 700; font-size: 45px; color: var(--green-dark);
  }
  .knowledge .section-title { top: 114px; }

  .article-card {
    position: absolute; top: 225px; width: 356px; height: 483px; background: var(--white);
    border-radius: 14px; overflow: hidden; box-shadow: 0 4px 16px rgba(0,0,0,0.08);
  }
  .article-media { height: 210px; }
  .media-food { background: linear-gradient(150deg, #e9f1d8, #b9d68a 55%, #e8c27a); }
  .media-gym { background: linear-gradient(160deg, #3d3f44, #1f2024 60%, #6a6c70); }
  .media-tea { background: linear-gradient(150deg, #f3ead6, #d8b36a 55%, #9bbf6a); }
  .article-body { padding: 0 20px 0 30px; }
  .article-tag {
    margin-top: 31px; font-family: 'Montserrat', sans-serif; font-weight: 600; font-size: 13px;
    color: var(--green-lime); text-transform: uppercase; letter-spacing: 0.3px;
  }
  .article-title {
    margin-top: 12px; font-family: 'Montserrat', sans-serif; font-weight: 700; font-size: 24px;
    line-height: 30px; color: var(--green-dark);
  }
  .article-excerpt { margin-top: 17px; font-size: 15.5px; line-height: 22.5px; color: var(--text-body); height: 68px; }
  .read-more {
    margin-top: 22px; display: flex; align-items: center; gap: 8px;
    font-size: 16px; color: var(--green-dark); text-decoration: none;
  }

  .cta .section-title { top: 912px; }
</style>
</head>
<body>
  <header class="site-header">
    <div class="brand"><span class="brand-dot"></span><span class="brand-name">THI</span></div>
    <nav class="main-nav">
      <a href="#" style="left:222px">Home</a>
      <a href="#" style="left:292px">About Us</a>
      <a href="#" style="left:387px">Therapies</a>
      <a href="#" style="left:487px">Team</a>
      <a href="#" style="left:555px">Knowledge</a>
      <a href="#" class="active" style="left:663px">Contact</a>
    </nav>
    <a href="#" class="webshop-link">Our Webshop</a>
    <a href="#" class="book-btn">Book Appointment</a>
  </header>

  <section class="knowledge">
    <h2 class="section-title">From Our Knowledge Center</h2>

    <article class="article-card" style="left:22px">
      <div class="article-media media-food" role="img" aria-label="Photo of healthy food"></div>
      <div class="article-body">
        <p class="article-tag">Nutrition</p>
        <h3 class="article-title">The Power of a Balanced Diet</h3>
        <p class="article-excerpt">Discover how the right nutrients can transform your health and well-being from the inside out...</p>
        <a href="#" class="read-more">Read More
          <svg width="16" height="10" viewBox="0 0 16 10"><path d="M0 5h14M10 1l4 4-4 4" fill="none" stroke="currentColor" stroke-width="1.6"/></svg></a>
      </div>
    </article>

    <article class="article-card" style="left:415px">
      <div class="article-media media-gym" role="img" aria-label="Photo of a man resting on a bench in a dark gym"></div>
      <div class="article-body">
        <p class="article-tag">Mindfulness</p>
        <h3 class="article-title">Finding Calm in a Busy World</h3>
        <p class="article-excerpt">Learn simple mindfulness techniques to reduce stress and improve your mental clarity every day...</p>
        <a href="#" class="read-more">Read More
          <svg width="16" height="10" viewBox="0 0 16 10"><path d="M0 5h14M10 1l4 4-4 4" fill="none" stroke="currentColor" stroke-width="1.6"/></svg></a>
      </div>
    </article>

    <article class="article-card" style="left:808px">
      <div class="article-media media-tea" role="img" aria-label="Photo of herbal tea"></div>
      <div class="article-body">
        <p class="article-tag">Herbal Remedies</p>
        <h3 class="article-title">Natural Solutions for Common Ailments</h3>
        <p class="article-excerpt">Explore the benefits of herbal medicine and how it can support your body's healing processes...</p>
        <a href="#" class="read-more">Read More
          <svg width="16" height="10" viewBox="0 0 16 10"><path d="M0 5h14M10 1l4 4-4 4" fill="none" stroke="currentColor" stroke-width="1.6"/></svg></a>
      </div>
    </article>
  </section>

  <section class="cta">
    <h2 class="section-title">Ready to Start Your Journey?</h2>
  </section>
</body>
</html>
```